Move the hackers to Wordpress

Yep, we want to move https://www.brasslantern.com/ to Wordpress. It'll make it easier to update and add content. I'd like mostly the same look, but I'm not stuck with it.
Updates

DO NOT RESPOND OUTSIDE OF PIXEL BAZAAR OR CONTACT US DIRECTLY.

Industry/Entity Type

Computer Security

Coding

Coded - Design and coding required

Font styles to use
Sans Serif

Colors
ec1f27

Requirements
Must have
• What I do want is:
• 1. Similar look to the existing site
• 2. Needs to work on one of the Wordpress hosting sites. I do NOT want to run my own Wordpress server.
• 3. Keep the animation in the top panel.
• 4. Mobile support
• The rest can be changed as needed.
Nice to have
• I like the transitions when the "services" panel shows up. Not stuck on it, but it is a nice touch.

```html
<!DOCTYPE html>
<html lang="en">
<head>
<meta charset="utf-8">
<title>Brass Lantern Information Security</title>
<link rel="stylesheet" href="https://fonts.googleapis.com/css2?family=Questrial&family=Arimo:ital,wght@0,400;0,700;1,400&display=swap">
<style>
:root{
  --red:#ec1f27;
  --red-deep:#d7262d;
  --ink:#111111;
  --charcoal:#353535;
  --charcoal-dark:#262626;
  --white:#ffffff;
  --grey-tab:#e6e6e6;
  --text:#333333;
  --muted:#555555;
  --field:rgba(255,255,255,.32);
}
*{box-sizing:border-box;margin:0;padding:0}
html,body{width:1200px;height:2663px;overflow:hidden;background:var(--white)}
body{position:relative;font-family:"Arimo",Arial,sans-serif;color:var(--text)}
.abs{position:absolute}
.heading{font-family:"Questrial",sans-serif;font-weight:400}

/* hero */
.hero{left:0;top:0;width:1200px;height:660px;background:radial-gradient(ellipse at 50% 40%,#3d3d3d 0%,#333 55%,#2b2b2b 100%)}
.phone-tab{left:737px;top:0;width:463px;height:36px;background:var(--grey-tab);clip-path:polygon(22px 0,100% 0,100% 100%,0 100%);display:flex;align-items:center;padding-left:58px;gap:10px;font-size:19px;color:var(--ink)}
.phone-tab .dot{width:26px;height:26px;border-radius:50%;background:var(--red);display:flex;align-items:center;justify-content:center}
.phone-tab .social{width:24px;height:24px;border-radius:50%;background:var(--ink)}
.phone-tab .social.red{background:var(--red)}
.brand{left:163px;top:28px;display:flex;align-items:center;gap:12px}
.brand .mark{width:40px;height:40px;background:var(--red)}
.brand .name{font-family:"Questrial",sans-serif;font-size:30px;letter-spacing:3px;color:var(--white)}
.nav{left:634px;top:58px;display:flex;gap:24px;font-family:"Questrial",sans-serif;font-size:17px;color:var(--white)}
.hero-title{left:0;top:255px;width:1200px;text-align:center;font-size:48px;line-height:69px;color:var(--white)}
.hero-title em{font-style:normal;color:var(--red)}

/* sections */
.section-title{width:1200px;left:0;text-align:center;font-size:35px;color:var(--ink)}
.section-title::after{content:"";display:block;width:34px;height:2px;background:var(--ink);margin:8px auto 0}
.section-title em{font-style:normal;color:var(--red)}
.what{left:0;top:660px;width:1200px;height:267px;background:var(--white)}
.what .lead{left:0;top:103px;width:1200px;text-align:center;color:var(--red);font-size:15px}
.what .body{left:181px;top:135px;width:841px;text-align:center;font-size:13px;line-height:22px;color:var(--text)}

.services{left:0;top:927px;width:1200px;height:426px;background:linear-gradient(180deg,var(--red-deep),#d92229)}
.services .section-title,.about .section-title{color:var(--white)}
.services .section-title::after,.about .section-title::after{background:var(--white)}
.service{top:120px;width:150px;text-align:center;font-size:11px;line-height:14px;color:var(--ink)}
.service svg{display:block;margin:0 auto 24px}
.service-note{left:170px;top:273px;width:856px;height:78px;border-radius:14px;background:rgba(255,255,255,.28);color:var(--white);font-size:13px;line-height:22px;text-align:center;padding:14px 34px}

.about{left:0;top:1353px;width:1200px;height:298px;background:linear-gradient(180deg,#3a3a3a 0%,#2c2c2c 60%,#3b3b3b 100%)}
.about .intro{left:0;top:124px;width:1200px;text-align:center;color:var(--white);font-size:15px}
.video-frame{left:218px;top:1530px;width:762px;height:405px;border:1px solid var(--red);background:var(--white)}
.video{left:10px;top:8px;width:740px;height:387px;background:radial-gradient(ellipse at 45% 45%,#4a5563 0%,#2a2f36 45%,#151719 100%)}
.play{left:340px;top:162px;width:62px;height:62px;border-radius:50%;background:rgba(200,200,200,.75)}
.controls{left:10px;top:338px;width:720px;height:42px;background:rgba(20,20,20,.55);border-radius:4px;color:var(--white);font-size:15px}
.controls .track{left:64px;top:19px;width:510px;height:6px;border-radius:3px;background:#bbb}
.controls .knob{left:64px;top:15px;width:50px;height:14px;border-radius:7px;background:#eee}
.controls .time{left:600px;top:12px}

.testimonials{left:0;top:1953px;width:1200px;height:319px}
.quote-badge{left:573px;top:111px;width:54px;height:54px;border-radius:50%;border:2px solid var(--red);color:var(--red);font-family:Georgia,serif;font-size:34px;text-align:center;line-height:62px}
.quote{left:0;top:186px;width:1200px;text-align:center;font-style:italic;font-size:14px;line-height:25px;color:var(--ink)}
.quote-by{left:0;top:250px;width:1200px;text-align:center;font-size:15px;color:var(--muted)}
.arrow{top:167px}

.contact{left:0;top:2272px;width:1200px;height:341px;background:var(--red-deep)}
.contact h3{left:163px;top:52px;font-size:23px;color:var(--white)}
.contact-item{left:163px;display:flex;gap:14px;color:var(--white);font-size:13px;line-height:20px}
.contact-item strong{font-weight:700}
.field{background:var(--field);color:var(--white);font-size:11px;padding:8px 12px}
.submit{left:641px;top:263px;width:85px;height:35px;background:var(--ink);color:var(--white);font-size:14px;font-weight:700;letter-spacing:1px;text-align:center;line-height:35px}

.footer{left:0;top:2613px;width:1200px;height:50px;background:var(--ink);color:var(--white);font-size:11px}
.footer .copy{left:163px;top:18px}
.footer .brand-small{left:888px;top:13px;display:flex;align-items:center;gap:8px;font-family:"Questrial",sans-serif;font-size:19px;letter-spacing:2px}
.footer .brand-small span{width:22px;height:22px;background:var(--red)}
</style>
</head>
<body>

<header class="hero abs" role="img" aria-label="Dark background with a network of thin grey lines joined at glowing red points">
  <div class="phone-tab abs">
    <span class="dot"><svg width="14" height="14" viewBox="0 0 24 24"><path fill="#fff" d="M6.6 10.8a15.1 15.1 0 0 0 6.6 6.6l2.2-2.2c.3-.3.7-.4 1-.2 1.1.4 2.3.6 3.6.6.6 0 1 .4 1 1V20c0 .6-.4 1-1 1A17 17 0 0 1 3 4c0-.6.4-1 1-1h3.5c.6 0 1 .4 1 1 0 1.3.2 2.5.6 3.6.1.3 0 .7-.2 1z"/></svg></span>
    <span>+1.555.204.8890</span>
    <span class="social red"></span><span class="social"></span><span class="social"></span>
  </div>
  <div class="brand abs"><span class="mark"></span><span class="name">BRASS LANTERN</span></div>
  <nav class="nav abs"><span>What We Do</span><span>Services</span><span>Blog</span><span>Press</span><span>Contact Us</span></nav>
  <h1 class="hero-title heading abs"><em>OFFENSIVE</em> SERVICES<br>FROM <em>OFFENSIVE</em> MINDS</h1>
</header>

<section class="what abs">
  <h2 class="section-title heading abs" style="top:38px">What <em>We Do</em></h2>
  <p class="lead abs">We are an information security company focusing on real world threats.</p>
  <p class="body abs">Brass Lantern is an information security consulting company that concentrates on the latest threats to organizations today. We perform in-depth analysis, determine organization/business risk, and find the vulnerabilities before the bad guys do. Our team includes internationally renowned experts who have been featured in international news outlets and conferences, including The Morning Ledger, The Capital Courier, a Pacific News Network Documentary.</p>
</section>

<section class="services abs">
  <h2 class="section-title heading abs" style="top:34px">Our <em style="color:#fff">Services</em></h2>
  <div class="service abs" style="left:134px"><svg width="62" height="46" viewBox="0 0 62 46" fill="none" stroke="#111" stroke-width="3"><rect x="4" y="3" width="40" height="28"/><path d="M16 42h18M25 31v11"/><rect x="46" y="16" width="12" height="24"/></svg>Internal Pivot<br>Assessment &amp; Post<br>Exploitation</div>
  <div class="service abs" style="left:298px"><svg width="62" height="46" viewBox="0 0 62 46" fill="#111"><circle cx="31" cy="12" r="8"/><circle cx="15" cy="18" r="6"/><circle cx="47" cy="18" r="6"/><path d="M18 44c0-12 26-12 26 0zM4 40c0-9 18-9 18 0zM40 40c0-9 18-9 18 0z"/></svg>Red Team Adversary<br>Simulation</div>
  <div class="service abs" style="left:456px"><svg width="62" height="46" viewBox="0 0 62 46" fill="none" stroke="#fff" stroke-width="3"><path d="M8 4h46M31 4v8"/><rect x="6" y="14" width="22" height="28"/><rect x="34" y="14" width="22" height="12"/><rect x="34" y="30" width="22" height="12"/><circle cx="17" cy="28" r="5" stroke="#111"/></svg>Penetration Testing<br>&amp; Vulnerability<br>Assessments</div>
  <div class="service abs" style="left:610px"><svg width="62" height="46" viewBox="0 0 62 46" fill="none" stroke="#111" stroke-width="3"><circle cx="31" cy="23" r="20"/><circle cx="31" cy="23" r="13"/><circle cx="31" cy="23" r="6"/></svg>Advanced Product,<br>Hardware &amp; RF<br>Testing</div>
  <div class="service abs" style="left:759px"><svg width="62" height="46" viewBox="0 0 62 46" fill="none" stroke="#111" stroke-width="3"><rect x="14" y="3" width="44" height="32"/><path d="M28 42h18M37 35v7"/><rect x="30" y="17" width="12" height="10" fill="#fff" stroke="#fff"/><path d="M32 17v-4a4 4 0 0 1 8 0v4" stroke="#fff"/><circle cx="8" cy="24" r="5"/><path d="M8 29v14"/></svg>Web Application<br>Penetration<br>Testing</div>
  <div class="service abs" style="left:907px"><svg width="62" height="46" viewBox="0 0 62 46" fill="none" stroke="#111" stroke-width="3"><rect x="19" y="2" width="22" height="42" rx="3"/><circle cx="38" cy="26" r="7"/><path d="M43 31l7 7"/></svg>Mobile Application<br>Assessment</div>
  <p class="service-note abs">This includes vulnerability scans of the in-scope systems where we manually verify issues and exploit any issues found. We report on the issues that actually have a real risk to your organization.</p>
</section>

<section class="about abs" role="img" aria-label="Dim city skyline at dusk behind the section">
  <h2 class="section-title heading abs" style="top:60px">About Us</h2>
  <p class="intro abs">We focus on hacking. This is our passion. We find the vulnerabilities before the bad guys do.</p>
</section>

<div class="video-frame abs">
  <div class="video abs" role="img" aria-label="Video still: close view of glasses reflecting a bright screen">
    <div class="play abs"><svg width="62" height="62" viewBox="0 0 62 62"><path d="M26 21l15 10-15 10z" fill="#ec1f27"/></svg></div>
    <div class="controls abs">
      <svg class="abs" style="left:20px;top:11px" width="20" height="20" viewBox="0 0 20 20"><path d="M3 1l15 9-15 9z" fill="#fff"/></svg>
      <div class="track abs"></div><div class="knob abs"></div>
      <span class="time abs">0:02</span>
      <svg class="abs" style="left:650px;top:11px" width="20" height="20" viewBox="0 0 20 20"><path d="M2 7h4l5-4v14l-5-4H2z" fill="#aaa"/></svg>
      <svg class="abs" style="left:685px;top:11px" width="20" height="20" viewBox="0 0 20 20"><rect x="1" y="3" width="18" height="14" fill="none" stroke="#ccc" stroke-width="2"/></svg>
    </div>
  </div>
</div>

<section class="testimonials abs">
  <h2 class="heading abs" style="left:0;top:40px;width:1200px;text-align:center;font-size:35px;color:#111">Clients Testimonials</h2>
  <div class="quote-badge abs">&ldquo;</div>
  <p class="quote abs">I read the report yesterday.<br>This is one of the best-written, actionable pentest reports I've ever seen.</p>
  <p class="quote-by abs">R.M. (Undisclosed Organization)</p>
  <svg class="arrow abs" style="left:138px" width="26" height="50" viewBox="0 0 26 50"><path d="M24 2L2 25l22 23" fill="none" stroke="#bbb" stroke-width="2"/></svg>
  <svg class="arrow abs" style="left:1043px" width="26" height="50" viewBox="0 0 26 50"><path d="M2 2l22 23L2 48" fill="none" stroke="#bbb" stroke-width="2"/></svg>
</section>

<section class="contact abs">
  <h3 class="heading abs">Contact Us</h3>
  <div class="contact-item abs" style="top:100px"><svg width="16" height="22" viewBox="0 0 16 22"><path d="M8 0a8 8 0 0 0-8 8c0 6 8 14 8 14s8-8 8-14a8 8 0 0 0-8-8zm0 11a3 3 0 1 1 0-6 3 3 0 0 1 0 6z" fill="#fff"/></svg><span><strong>BRASS LANTERN INFORMATION SECURITY</strong><br>Street Name, City Name<br>State Zipcode</span></div>
  <div class="contact-item abs" style="top:190px"><svg width="18" height="18" viewBox="0 0 24 24"><path fill="#fff" d="M6.6 10.8a15.1 15.1 0 0 0 6.6 6.6l2.2-2.2c.3-.3.7-.4 1-.2 1.1.4 2.3.6 3.6.6.6 0 1 .4 1 1V20c0 .6-.4 1-1 1A17 17 0 0 1 3 4c0-.6.4-1 1-1h3.5c.6 0 1 .4 1 1 0 1.3.2 2.5.6 3.6.1.3 0 .7-.2 1z"/></svg><span>+1.555.204.8890</span></div>
  <div class="contact-item abs" style="top:235px"><svg width="18" height="16" viewBox="0 0 18 16"><path d="M1 6l8-5 8 5v9H1z M1 6l8 5 8-5" fill="none" stroke="#fff" stroke-width="1.8"/></svg><span>contact@brasslantern.com</span></div>
  <div class="field abs" style="left:641px;top:45px;width:397px;height:35px">Name</div>
  <div class="field abs" style="left:641px;top:89px;width:193px;height:34px">Email</div>
  <div class="field abs" style="left:845px;top:89px;width:193px;height:34px">Mobile</div>
  <div class="field abs" style="left:641px;top:135px;width:397px;height:113px">Message</div>
  <div class="submit abs">Submit</div>
</section>

<footer class="footer abs">
  <p class="copy abs">Copyright © 2018 Brass Lantern Information Security.&nbsp; I&nbsp; All Rights Reserved.</p>
  <div class="brand-small abs"><span></span>BRASS LANTERN</div>
</footer>

</body>
</html>
```